Brochure and Vector Design Project

We have a 33 page report done in Powerpoint that needs to be created into a PDF. The tables and graphs are very standard and we need them to stand out and look great! We can provide fonts and brand guidelines.

Format:
Re-skin a number of graphs that will support The Bright & Outcome research report. The graphs have already been developed, however they need to be made to look on brand.
Design of and formatting of the KORV Creative Effectiveness Research report template.

You will be required to:
• Reskin a number of graphs (32)
• Develop a front and back page design
• Develop an interior page look and feel – This will then be replicated throughout the report.

Specs:
Vetor graph files to be supplied in a layered png and eps file.
Front/Back page design and interior page template (InDesign).

Purpose:
To visualise the results of the creative effectiveness research paper. This piece will be targeted at Agency staff, who tend to take things in visually rather than through text.

Guidelines: Please refer to the brand guidelines supplied. The graphs will primarily need to pull through the secondary purple colour as the main template will feature the purple.

We are collating a report which examines the trends emerging within agencies within Australia. This report will be made available to our members and will be distributed through the appropriate media partners. The purpose of the graphs is to add a visual representation of the report as well as increase engagement and readership.
Updates

Hi all,

The brand is very structured, so no need to patterns or gradients in the background with regards to where our logo sits.

The core design choice for us, will be great use of the graphs in the powerpoints. These are 'Standard' graphs and we'd like them to look great! (Not just *standard*)

Thank you.

KORV

Hi all,

Thank you.

KORV

Target Market(s)

Creative Directors, Art Directors, Creative Executives, Copywriters, Agency Staff

Industry/Entity Type

Media

Requirements
Must have
• Must use our brand guidelines and fonts.

```html
<!DOCTYPE html>
<html lang="en">
<head>
<meta charset="utf-8">
<title>KORV report charts – cover, chart page, back cover</title>
<link rel="stylesheet" href="https://fonts.googleapis.com/css2?family=Barlow:wght@400;500;600;800&display=swap">
<style>
  :root {
    --backdrop: #e9e6e1;
    --paper: #ffffff;
    --paper-shade: #f1f2f4;
    --brand-red: #c8202a;
    --ink: #1f1f22;
    --ink-soft: #4a4a50;
    --grey-band: #8d8f94;
    --grey-dark: #55575c;
    --chart-purple: #5555a3;
    --chart-purple-edge: #2d2d66;
    --tile: #e3e8ef;
    --photo-deep: #0a2f66;
    --photo-light: #3f8fd8;
  }
  * { box-sizing: border-box; margin: 0; padding: 0; }
  html, body { width: 1200px; height: 562px; overflow: hidden; }
  body {
    background: var(--backdrop);
    font-family: "Barlow", Arial, sans-serif;
    color: var(--ink);
    position: relative;
  }
  .page {
    position: absolute;
    top: 20px;
    width: 370px;
    height: 522px;
    background: linear-gradient(180deg, var(--paper) 0%, var(--paper-shade) 100%);
    box-shadow: 0 2px 6px rgba(0,0,0,.18);
    overflow: hidden;
  }
  .page--cover { left: 20px; }
  .page--chart { left: 414px; }
  .page--back  { left: 810px; }

  .wordmark {
    position: absolute;
    font-weight: 800;
    color: var(--ink);
    letter-spacing: -1px;
    line-height: 1;
  }
  .wordmark__descriptor {
    position: absolute;
    font-size: 5px;
    font-weight: 600;
    color: var(--ink);
    white-space: nowrap;
  }

  .chevron { display: inline-block; vertical-align: middle; }

  /* Cover */
  .cover__photo {
    position: absolute; left: 0; top: 30px; width: 370px; height: 228px;
    background: radial-gradient(ellipse at 55% 40%, var(--photo-light) 0%, #1d5fae 45%, var(--photo-deep) 100%);
  }
  .cover__strap {
    position: absolute; left: 0; top: 258px; width: 370px; height: 34px;
    background: var(--brand-red);
    color: #fff; font-size: 12px; font-weight: 500;
    display: flex; align-items: center; padding-left: 76px; gap: 8px;
  }
  .cover__tiles {
    position: absolute; left: 0; top: 372px; width: 370px; height: 96px;
    background: linear-gradient(180deg, rgba(227,232,239,0) 0%, var(--tile) 45%, rgba(227,232,239,0) 100%);
  }
  .cover__title {
    position: absolute; left: 0; top: 356px; width: 370px; text-align: center;
    font-size: 21px; font-weight: 500; color: var(--ink);
  }
  .cover__wordmark { left: 246px; top: 428px; font-size: 38px; }
  .cover__descriptor { left: 246px; top: 463px; }
  .swoosh { position: absolute; left: 0; bottom: 0; }
  .cover__url {
    position: absolute; right: 24px; bottom: 14px; color: #fff; font-size: 7px;
  }

  /* Chart page */
  .chart__header {
    position: absolute; left: 16px; top: 24px; width: 240px; height: 18px;
    background: var(--brand-red); border-radius: 9px;
    color: #fff; font-size: 7.5px; font-weight: 500;
    display: flex; align-items: center;
  }
  .chart__pagenum {
    width: 21px; height: 26px; background: var(--ink); margin-left: 28px;
    display: flex; align-items: center; justify-content: center; font-size: 7px;
  }
  .chart__header-text { display: flex; align-items: center; gap: 5px; margin-left: 14px; }
  .chart__wordmark { left: 276px; top: 22px; font-size: 25px; }
  .chart__descriptor { left: 276px; top: 45px; font-size: 3.5px; }
  .rule { position: absolute; height: 1.5px; background: var(--brand-red); }
  .chart__title {
    position: absolute; left: 0; top: 113px; width: 370px; text-align: center;
    font-size: 18px; font-weight: 500; line-height: 23px;
  }
  .chart__plot { position: absolute; left: 0; top: 0; }
  .chart__address {
    position: absolute; right: 8px; top: 478px; text-align: right;
    color: #fff; font-size: 6px; line-height: 10px;
  }
  .chart__contacts {
    position: absolute; left: 0; bottom: 4px; width: 370px; text-align: center;
    color: #fff; font-size: 5.5px;
  }
  .chart__contacts b { color: var(--brand-red); font-weight: 600; }

  /* Back */
  .back__tagline {
    position: absolute; left: 78px; top: 41px; font-size: 11px;
    display: flex; align-items: center; gap: 7px; color: var(--ink);
  }
  .back__tiles {
    position: absolute; left: 0; top: 212px; width: 370px; height: 92px;
    background: linear-gradient(180deg, rgba(227,232,239,.4) 0%, var(--tile) 50%, rgba(227,232,239,.4) 100%);
  }
  .back__wordmark { left: 130px; top: 238px; font-size: 34px; }
  .back__descriptor { left: 130px; top: 270px; }
  .back__address {
    position: absolute; left: 56px; top: 464px; font-size: 5.5px; line-height: 9px; color: var(--ink-soft);
  }
  .back__address b { font-weight: 600; color: var(--ink); }
  .back__address .tag { color: var(--brand-red); font-weight: 600; }
</style>
</head>
<body>

<section class="page page--cover">
  <div class="cover__photo" role="img" aria-label="Photo: woman touching a glowing digital interface over a blue world map"></div>
  <div class="cover__strap">
    <svg class="chevron" width="12" height="16" viewBox="0 0 12 16"><path d="M2 1 L9 8 L2 15" fill="none" stroke="#fff" stroke-width="2.4"/></svg>
    Marketing &amp; advertising at the speed of life.
  </div>
  <div class="cover__tiles"></div>
  <h1 class="cover__title">KORV report charts</h1>
  <div class="wordmark cover__wordmark">KORV</div>
  <div class="wordmark__descriptor cover__descriptor">Society for insight-led marketing &amp; media</div>
  <svg class="swoosh" width="370" height="52" viewBox="0 0 370 52">
    <defs><linearGradient id="swooshGrey" x1="0" x2="1"><stop offset="0" stop-color="#d8d9dc"/><stop offset=".5" stop-color="#9a9ca1"/><stop offset="1" stop-color="#5a5c61"/></linearGradient></defs>
    <path d="M0 52 L0 40 C130 40 160 6 240 6 L370 6 L370 52 Z" fill="url(#swooshGrey)"/>
  </svg>
  <div class="cover__url">www.korv.org.au</div>
</section>

<section class="page page--chart">
  <div class="chart__header">
    <div class="chart__pagenum">1</div>
    <div class="chart__header-text">
      <svg class="chevron" width="7" height="10" viewBox="0 0 7 10"><path d="M1 1 L5 5 L1 9" fill="none" stroke="#fff" stroke-width="1.6"/></svg>
      Marketing &amp; advertising at the speed of life.
    </div>
  </div>
  <div class="wordmark chart__wordmark">KORV</div>
  <div class="wordmark__descriptor chart__descriptor">Society for insight-led marketing &amp; media</div>

  <div class="rule" style="left:22px;top:102px;width:328px"></div>
  <h2 class="chart__title">Fig 1. The number of top-box business<br>effects correlates well with profit growth</h2>
  <div class="rule" style="left:22px;top:163px;width:328px"></div>

  <svg class="chart__plot" width="370" height="430" viewBox="0 0 370 430" font-family="Barlow, Arial, sans-serif">
    <g font-size="6.5" fill="#222" text-anchor="end">
      <text x="58" y="388">0%</text><text x="58" y="373">10%</text><text x="58" y="357">20%</text>
      <text x="58" y="342">30%</text><text x="58" y="327">40%</text><text x="58" y="311">50%</text>
      <text x="58" y="296">60%</text><text x="58" y="281">70%</text><text x="58" y="265">80%</text>
      <text x="58" y="250">90%</text><text x="58" y="235">100%</text>
    </g>
    <g stroke="#444" stroke-width=".8">
      <line x1="63" y1="232" x2="63" y2="386"/>
      <line x1="63" y1="386" x2="354" y2="386"/>
    </g>
    <g fill="var(--chart-purple)" stroke="var(--chart-purple-edge)" stroke-width=".8">
      <rect x="76"  y="373.7" width="19" height="12.3"/>
      <rect x="117" y="355.2" width="19" height="30.8"/>
      <rect x="159" y="366"   width="19" height="20"/>
      <rect x="201" y="304.4" width="19" height="81.6"/>
      <rect x="242" y="267.4" width="19" height="118.6"/>
      <rect x="284" y="279.7" width="19" height="106.3"/>
      <rect x="325" y="252"   width="19" height="134"/>
    </g>
    <g font-size="8.5" fill="#222" text-anchor="middle">
      <text x="85" y="369">8%</text><text x="126" y="351">20%</text><text x="168" y="362">13%</text>
      <text x="210" y="300">53%</text><text x="251" y="263">77%</text><text x="293" y="275">69%</text>
      <text x="334" y="248">87%</text>
    </g>
    <g font-size="7" fill="#222" text-anchor="middle">
      <text x="85" y="398">0</text><text x="126" y="398">1</text><text x="168" y="398">2</text>
      <text x="210" y="398">3</text><text x="251" y="398">4</text><text x="293" y="398">5</text>
      <text x="334" y="398">6</text>
      <text x="206" y="411">Reported number of top-box business effects excluding profit</text>
    </g>
    <text transform="translate(26 309) rotate(-90)" font-size="7" fill="#222" text-anchor="middle">% Campaigns reporting top box</text>
    <text transform="translate(35 309) rotate(-90)" font-size="7" fill="#222" text-anchor="middle">profit growth</text>
  </svg>

  <div class="rule" style="left:22px;top:428px;width:328px"></div>

  <svg class="swoosh" width="370" height="56" viewBox="0 0 370 56">
    <defs><linearGradient id="swooshGreyMid" x1="0" x2="1"><stop offset="0" stop-color="#d8d9dc"/><stop offset=".5" stop-color="#9a9ca1"/><stop offset="1" stop-color="#6a6c71"/></linearGradient></defs>
    <path d="M0 56 L0 36 C130 36 160 2 240 2 L370 2 L370 56 Z" fill="url(#swooshGreyMid)"/>
    <rect x="0" y="34" width="370" height="22" fill="var(--grey-dark)"/>
  </svg>
  <div class="chart__address"><b>OFFICE</b> Level 4, 18 Harbour Lane,<br>Sydney NSW 2000 / <b>POSTAL</b> GPO Box 1120 NSW 2001</div>
  <div class="chart__contacts"><b>t.</b> (02) 9100 2200 &nbsp;<b>f.</b> (02) 9100 2210 &nbsp;<b>e.</b> info@korv.org.au &nbsp;<b>w.</b> korv.org.au &nbsp; ABN 11 222 333 444</div>
</section>

<section class="page page--back">
  <div class="back__tagline">
    <svg class="chevron" width="14" height="14" viewBox="0 0 14 14"><path d="M1 1 L7 7 L1 13 M6 1 L12 7 L6 13" fill="none" stroke="var(--brand-red)" stroke-width="2"/></svg>
    Marketing &amp; advertising at the speed of life.
  </div>
  <div class="back__tiles"></div>
  <div class="wordmark back__wordmark">KORV</div>
  <div class="wordmark__descriptor back__descriptor">Society for insight-led marketing &amp; media</div>
  <div class="rule" style="left:48px;top:458px;width:274px"></div>
  <div class="back__address">
    <b>OFFICE</b> Level 4, 18 Harbour Lane, Sydney NSW 2000 / <b>POSTAL</b> GPO Box 1120 NSW 2001<br>
    <span class="tag">t.</span> (02) 9100 2200 &nbsp;<span class="tag">f.</span> (02) 9100 2210 &nbsp;<span class="tag">e.</span> info@korv.org.au &nbsp;<span class="tag">w.</span> korv.org.au &nbsp; ABN 11 222 333 444
  </div>
</section>

</body>
</html>
```